food label design

we need a label design for honey, we are beekeepers in WA/ Western Australia we produce many type of honey, so the label should suit all types. either by changing the name or colour variation etc, There is many great designs we have seen on google. But the design we had was not satisfying, maybe because we have seen many good ones that the design didn't impress us. We would like something that can be called premium and also unique
Updates

Target Market(s)

food, honey

Logo Text

copper wren

Font styles to use
Serif
Sans Serif
Decorative
Script

Colors

Designer to choose colors to be used in the design.

Requirements
Nice to have
• since the package already includes the logo design, could you guys just add the new logo design into the label? since that would make my selection of the winning project easier.
• the original logo, it did look nice but im not sure if its ok to have copper select wren in the logo so yea. looking forward to see some new and better designs.
• Also it would be nice if designers can include the sizes of the label, or just some suggestion that could make it look better. since the size will affect like the word font etc bottle have different sizes.
• Also if can show the design on a honey bottle will be nice, we currently use hexagon bottle would consider cylinder in the future so if the design can include these would be perfect.
Should not have
• the attachment i included is the label design i have at the moment, it is nice but im not very impressed with it. Since one of the beekeepers in my State use almost the same design just different colour

```html
<!DOCTYPE html>
<html lang="en">
<head>
<meta charset="utf-8">
<title>Copper Wren – Honey Label Set</title>
<link rel="stylesheet" href="https://fonts.googleapis.com/css2?family=Arimo:wght@400;700&family=Oswald:wght@500&display=swap">
<style>
  :root {
    --backdrop: #eceeef;
    --honey-light: #f1c320;
    --honey-amber: #f0b02c;
    --honey-orange: #e4813a;
    --ink: #2a1f0a;
    --ink-soft: #3d2c0f;
    --comb-light: rgba(255, 230, 140, 0.35);
    --comb-orange: rgba(255, 200, 150, 0.3);
  }
  * { margin: 0; padding: 0; box-sizing: border-box; }
  html, body {
    width: 1200px; height: 800px; overflow: hidden;
    background: var(--backdrop);
    font-family: "Arimo", Arial, sans-serif;
    color: var(--ink);
  }
  .label-set { position: relative; width: 1200px; height: 800px; }
  .label {
    position: absolute; top: 336px; width: 268px; height: 296px;
    border-radius: 14px; overflow: hidden;
  }
  .label--back { left: 168px; background: linear-gradient(180deg, #f3c822, var(--honey-light) 70%, #e9b91c); }
  .label--front { left: 466px; background: linear-gradient(180deg, #f2b731, var(--honey-amber) 70%, #e7a526); }
  .label--nutrition { left: 766px; background: linear-gradient(180deg, #e98a3e, var(--honey-orange) 70%, #dc7733); }

  .comb-field { position: absolute; border-radius: 4px; }
  .label--back .comb-field { left: 24px; top: 80px; width: 110px; height: 190px;
    background: linear-gradient(135deg, var(--comb-light), transparent 80%); }
  .label--nutrition .comb-field { right: 10px; top: 70px; width: 70px; height: 200px;
    background: linear-gradient(200deg, var(--comb-orange), transparent 85%); }

  .txt { position: absolute; line-height: 1.2; }

  /* back label */
  .intro { left: 60px; top: 86px; width: 200px; font-size: 7px; }
  .intro .brand { font-size: 10.5px; margin-right: 8px; }
  .story { left: 60px; top: 120px; width: 178px; font-size: 6.8px; }
  .claim { left: 0; width: 100%; top: 154px; font-size: 8.5px; text-align: center; }
  .producer { left: 60px; top: 180px; font-size: 7px; }
  .contact { left: 60px; top: 196px; font-size: 6.8px; }

  /* front label */
  .brand-lockup { left: 0; width: 100%; top: 116px; text-align: center; }
  .brand-lockup .mark-dot {
    display: block; width: 14px; height: 14px; margin: 0 auto 8px;
    border-radius: 50%; background: var(--ink);
  }
  .brand-lockup .brand-name {
    font-family: "Oswald", "Arial Narrow", sans-serif; font-weight: 500;
    font-size: 20px; letter-spacing: 2px; text-transform: uppercase; color: var(--ink);
  }
  .flavour {
    left: 0; width: 100%; top: 214px; text-align: center;
    font-family: "Oswald", "Arial Narrow", sans-serif; font-weight: 500;
    font-size: 27px; letter-spacing: 0.5px; color: #1c1408;
  }
  .origin { left: 0; width: 100%; top: 252px; text-align: center; font-size: 8px; letter-spacing: 1.4px; }

  /* nutrition label */
  .warning { left: 0; width: 100%; top: 90px; text-align: center; font-size: 7.2px; }
  .nutrition-table {
    position: absolute; left: 50px; top: 108px; width: 160px;
    border-collapse: collapse; font-size: 5.8px;
  }
  .nutrition-table th { font-weight: 400; font-size: 4.4px; text-align: left; padding-bottom: 6px; }
  .nutrition-table td { padding: 0; line-height: 1.25; }
  .nutrition-table .gap td { height: 8px; }
  .storage { left: 0; width: 100%; top: 204px; text-align: center; font-size: 6.8px; }
  .net { left: 0; width: 100%; top: 230px; text-align: center; font-size: 7.5px; }
</style>
</head>
<body>
<main class="label-set">

  <section class="label label--back">
    <div class="comb-field" role="img" aria-label="faint honeycomb pattern"></div>
    <p class="txt intro"><span class="brand">Copper Wren</span>passion in producing high quality<br>honey to our customers</p>
    <p class="txt story">Our honey is all natural, unheated and unprocessed, from the nectar of our western australian flowers, to bees then to you.</p>
    <p class="txt claim">100% Natural Australian Honey</p>
    <p class="txt producer">Produced and packed by: COPPER WREN</p>
    <p class="txt contact">14 Banksia Lane, Wattle Vale WA 6100<br>0400111222<br>www.copperwren.com.au</p>
  </section>

  <section class="label label--front">
    <div class="txt brand-lockup">
      <span class="mark-dot"></span>
      <span class="brand-name">Copper Select Wren</span>
    </div>
    <h1 class="txt flavour">CLOVER FLAVOUR</h1>
    <p class="txt origin">RAW WESTERN AUSTRALIAN HONEY</p>
  </section>

  <section class="label label--nutrition">
    <div class="comb-field" role="img" aria-label="faint honeycomb pattern"></div>
    <p class="txt warning">DO NOT GIVE TO INFANTS UNDER 12 MONTHS OLD</p>
    <table class="nutrition-table">
      <tr><th colspan="2">NUTRITION INFORMATION</th><th colspan="2" style="text-align:right">NET WEIGHT 250g</th></tr>
      <tr><th colspan="2">SERVINGS PER PACK APPROX 17</th><th>PER SERVING</th><th>PER 100g</th></tr>
      <tr><td>ENERGY</td><td></td><td>210KJ</td><td>1400KJ</td></tr>
      <tr><td>PROTEIN</td><td></td><td>0.0g</td><td>0.3g</td></tr>
      <tr><td>FAT, TOTAL</td><td></td><td>0.0g</td><td>0.0g</td></tr>
      <tr><td>CARBOHYDRATE</td><td></td><td>12.3g</td><td>82.1g</td></tr>
      <tr><td>SUGARS</td><td></td><td>12.3g</td><td>82.1g</td></tr>
      <tr><td>SODIUM</td><td></td><td>2mg</td><td>14mg</td></tr>
      <tr><td>ASH RESIDUE</td><td></td><td>0.1g</td><td>0.3g</td></tr>
      <tr><td>MOISTURE</td><td></td><td>0.1g</td><td>0.3g</td></tr>
    </table>
    <p class="txt storage">Store at room temperature<br>Do not Microwave/Refrigerate</p>
    <p class="txt net">250g</p>
  </section>

</main>
</body>
</html>
```